Australian Wine export company Need a Wine label design

We need a wine label design for a new branded Australian wine based in South Australia called " HALLORAN " .
We will use this brand name ' HALLORAN' to marketing Australian Red wine and White wine into Chinese Market.
We would like to see the label designs that look classic and make consumers feel this is a superior quality Australian wine.
This label is to promote AUSTRALIAN WINE, need wine related and country related theme, need to give the consumer first impression that this wine is from AUSTRALIA.

Thanks
Updates

The following information are required to be presented on the wine label:

1) Brand Name: Halloran
2) Logo
3) Year of Vintage
4) Varietal
5) Place of production: South Australia
6) Fine Wine of Australia

Thanks.

Target Market(s)

Chinese market

Industry/Entity Type

Marketing

Requirements
Must have
• Need label design and renderings on the bottles.
Nice to have
• Label make consumers feel this is a superior quality Australian Wine.

```html
<!DOCTYPE html>
<html lang="en">
<head>
<meta charset="utf-8">
<title>Halloran – Australian Red Wine Label</title>
<link href="https://fonts.googleapis.com/css2?family=Questrial&family=Arimo:wght@400&display=swap" rel="stylesheet">
<style>
  :root {
    --page: #ffffff;
    --frame: #111111;
    --frame-red: #e0191f;
    --silver-left: #b4b4b4;
    --silver-light: #fbfbfb;
    --silver-right: #5c5c5c;
    --ink: #0b0b0b;
    --wine-red: #d42a25;
    --wine-brown: #7a4a3c;
    --sprig: #8a2a22;
  }
  html, body {
    margin: 0;
    padding: 0;
    width: 1200px;
    height: 1000px;
    overflow: hidden;
    background: var(--page);
  }
  .canvas {
    position: relative;
    width: 1200px;
    height: 1000px;
  }
  .label {
    position: absolute;
    left: 309px;
    top: 137px;
    width: 582px;
    height: 726px;
    background: var(--frame);
  }
  .label::before,
  .label::after {
    content: "";
    position: absolute;
    left: 0;
    right: 0;
    height: 6px;
    background: linear-gradient(90deg, var(--frame) 0%, var(--frame-red) 50%, var(--frame) 100%);
  }
  .label::before { top: 0; }
  .label::after { bottom: 0; }
  .label-face {
    position: absolute;
    inset: 6px;
    background: linear-gradient(90deg,
      var(--silver-left) 0%,
      #c9c9c9 25%,
      var(--silver-light) 55%,
      #cfcfcf 72%,
      #a9a9a9 85%,
      var(--silver-right) 100%);
  }
  .brand-name {
    position: absolute;
    left: 0;
    right: 0;
    top: 80px;
    margin: 0;
    text-align: center;
    font-family: "Questrial", sans-serif;
    font-weight: 400;
    font-size: 136px;
    line-height: 1;
    color: var(--ink);
    letter-spacing: -1px;
  }
  .varietal {
    position: absolute;
    left: 0;
    right: 0;
    top: 372px;
    margin: 0;
    text-align: center;
    font-family: "Questrial", sans-serif;
    font-weight: 400;
    font-size: 41px;
    line-height: 1;
  }
  .varietal span {
    background: linear-gradient(90deg, #2a2222 0%, var(--wine-red) 45%, var(--wine-red) 60%, var(--wine-brown) 80%, #2a2222 100%);
    -webkit-background-clip: text;
    background-clip: text;
    color: transparent;
  }
  .vintage {
    position: absolute;
    left: 0;
    right: 0;
    top: 425px;
    margin: 0;
    text-align: center;
    font-family: "Arimo", sans-serif;
    font-size: 16px;
    color: var(--ink);
  }
  .sprig {
    position: absolute;
    left: 153px;
    top: 442px;
    width: 276px;
    height: 42px;
  }
  .details {
    position: absolute;
    left: 0;
    right: 0;
    top: 657px;
    margin: 0;
    text-align: center;
    font-family: "Arimo", sans-serif;
    font-size: 20px;
    line-height: 26px;
    color: var(--ink);
  }
</style>
</head>
<body>
  <main class="canvas">
    <section class="label">
      <div class="label-face">
        <h1 class="brand-name">Halloran</h1>
        <p class="varietal"><span>Australian Red Wine</span></p>
        <p class="vintage">2013</p>
        <svg class="sprig" viewBox="0 0 276 42" role="img" aria-label="Decorative laurel sprig with small red blossoms">
          <ellipse cx="138" cy="20" rx="136" ry="12" fill="var(--sprig)" opacity="0.35"/>
        </svg>
        <p class="details">700 mL<br>14% ALC/VOL</p>
      </div>
    </section>
  </main>
</body>
</html>
```